web site to find a reliable, local tradesman, handyman or builder for any job

Design a web site as marketplace for handyman and client.
Handyman can
* set their profile (name, address, contacts)
* search / view / apply for job offers (by setting a new offer)
Client can
* search / view job offers
* generate new job offers (title, description, max price, date, duration, location).
* select and rate a job
Main functions would be SEARCH / VIEW to see in one glance WHAT needs to be done WHERE. The contractors then exchange contacts.
Handyman

```html
<!DOCTYPE html>
<html lang="en">
<head>
<meta charset="utf-8">
<title>FIXWELL – Find a reliable tradesman</title>
<link rel="stylesheet" href="https://fonts.googleapis.com/css2?family=Montserrat:wght@300;400;500;600;700&display=swap">
<style>
:root{
  --navy:#0b2c78;
  --navy-deep:#08275f;
  --footer:#0a2a6c;
  --pill:#0a55cc;
  --orange:#ff7300;
  --orange-light:#ff9a2e;
  --sky-top:#86c2fb;
  --sky-bottom:#4e93e2;
  --about-blue:#5c9fe6;
  --text-grey:#666;
  --heading-grey:#444;
  --panel:#eeeeee;
  --white:#fff;
}
*{box-sizing:border-box;margin:0;padding:0}
html,body{width:1200px;height:1190px;overflow:hidden;background:var(--white)}
body{font-family:"Montserrat",Arial,sans-serif;position:relative}
.page{position:relative;width:1200px;height:1190px}
a{color:inherit;text-decoration:none}

/* header */
.site-header{position:absolute;left:0;top:0;width:1200px;height:80px;
  background:linear-gradient(#0d3288 0,#0d3288 38px,var(--navy-deep) 40px,var(--navy-deep) 100%);border-bottom:1px solid #2a5fb8}
.brand{position:absolute;left:150px;top:24px;display:flex;align-items:center;gap:10px;color:var(--white);font-weight:500;font-size:34px;letter-spacing:2px}
.brand-mark{width:14px;height:14px;background:var(--orange)}
.main-nav{position:absolute;top:24px;left:0;width:1200px;height:32px;font-size:12.5px;color:var(--white);letter-spacing:0}
.main-nav a{position:absolute;top:0;line-height:32px;white-space:nowrap}
.main-nav .active{background:var(--pill);border-radius:16px;width:88px;text-align:center}
.main-nav .sign-in{color:var(--orange);text-decoration:underline}

/* hero */
.hero{position:absolute;left:0;top:81px;width:1200px;height:421px;
  background:linear-gradient(180deg,var(--sky-top),#6aaaf0 50%,var(--sky-bottom));border-bottom:3px solid #3f86da}
.hero-photo{position:absolute;left:845px;top:44px;width:205px;height:377px;border-radius:100px 100px 0 0;
  background:linear-gradient(180deg,#f3d23a 0,#e8c9a8 22%,#f2f2f2 45%,#a07645 70%,#3f5f8e 100%);opacity:.9;z-index:1}
.hero-title{position:absolute;left:150px;top:72px;z-index:2;color:var(--white);font-size:34px;font-weight:400;line-height:49px;letter-spacing:-.2px;white-space:nowrap;text-shadow:0 1px 2px rgba(0,40,110,.25)}
.hero-title strong{font-weight:700}
.hero-copy{position:absolute;left:151px;top:188px;width:450px;color:var(--white);font-size:11.5px;line-height:17px}
.hero-button{position:absolute;left:150px;top:299px;width:205px;height:55px;border-radius:10px;
  background:linear-gradient(var(--orange-light),var(--orange));color:var(--white);font-size:25px;font-weight:300;display:flex;align-items:center;justify-content:center}
.hero-button span{border-bottom:1px solid rgba(255,255,255,.8);line-height:28px}
.slider-dots{position:absolute;left:151px;top:384px;display:flex;gap:6px}
.slider-dots i{width:14px;height:14px;border-radius:50%;background:var(--white)}
.slider-dots i:first-child{background:var(--orange)}

/* about */
.shade-line{position:absolute;left:180px;top:516px;width:920px;height:8px;background:radial-gradient(ellipse at center,rgba(0,0,0,.12),transparent 70%)}
.about{position:absolute;left:151px;top:530px;width:470px}
.about h2{font-size:41px;font-weight:300;color:var(--about-blue);line-height:50px}
.about p{margin-top:6px;font-size:11.6px;line-height:20px;color:var(--text-grey)}

.finder{position:absolute;left:643px;top:540px;width:407px;height:183px;background:var(--panel);border-radius:4px;font-size:14px;color:#444}
.finder-title{position:absolute;left:21px;top:12px;font-size:14px;color:#444}
.finder-title strong{color:var(--orange);font-size:19px;font-weight:600}
.finder label{position:absolute}
.field{position:absolute;height:22px;background:var(--white);border:1px solid #bbb;font:12px Arial,sans-serif;color:#222;padding:3px 5px}
.select::after{content:"";position:absolute;right:6px;top:8px;border:4px solid transparent;border-top:5px solid #111}
.finder-submit{position:absolute;left:232px;top:142px;width:151px;height:33px;border-radius:4px;background:linear-gradient(var(--orange-light),var(--orange));color:var(--white);font-size:12px;display:flex;align-items:center;justify-content:center}
.finder-submit strong{margin-left:4px;font-weight:700}

/* features */
.divider{position:absolute;left:0;top:742px;width:1200px;border-top:1px dashed #d8d8d8}
.feature{position:absolute;top:750px;width:252px}
.feature-icon{position:absolute;left:0;top:0;width:16px;height:38px;background:linear-gradient(#1d3f7a,#0e2750);border-radius:6px 6px 2px 2px}
.feature h3{margin-left:28px;font-size:19px;font-weight:500;color:var(--heading-grey);line-height:22px}
.feature p{margin-top:16px;font-size:11.6px;line-height:20px;color:var(--text-grey)}
.feature .callout{color:var(--orange);font-weight:600;font-size:13px;line-height:20px;text-decoration:underline;text-decoration-color:#ffc690}

/* footer */
.site-footer{position:absolute;left:0;top:898px;width:1200px;height:292px;background:var(--footer);color:var(--white)}
.site-footer h4{font-size:18px;font-weight:500;letter-spacing:1px}
.contacts{position:absolute;left:150px;top:26px}
.contacts p{margin-top:7px;font-size:14px;line-height:24px}
.contacts b{color:var(--orange);font-weight:600}
.message{position:absolute;left:480px;top:26px}
.input{position:absolute;background:var(--white);border:1px solid #9fb0d0;color:#777;font:14px Arial,sans-serif;padding:4px 6px}
.submit-btn{position:absolute;left:2px;top:193px;width:81px;height:33px;border-radius:4px;background:var(--orange);font-size:14px;display:flex;align-items:center;justify-content:center}
.follow{position:absolute;left:877px;top:26px}
.follow ul{list-style:none;margin-top:16px;font-size:12.5px}
.follow li{display:flex;align-items:center;gap:8px;height:22px;margin-bottom:10px;white-space:nowrap}
.follow li i{width:21px;height:21px;background:#5aa3e8;border-radius:3px}
.legal{position:absolute;left:0;top:260px;width:1200px;height:32px;border-top:1px solid #1f4590;font-size:13px}
.legal .copy{position:absolute;left:153px;top:6px}
.legal nav{position:absolute;left:403px;top:7px;font-size:11px;letter-spacing:.4px}
.legal nav span{margin:0 6px}
</style>
</head>
<body>
<div class="page">

<header class="site-header">
  <div class="brand"><i class="brand-mark"></i>FIXWELL</div>
  <nav class="main-nav">
    <a class="active" href="#" style="left:471px">NAME</a>
    <a href="#" style="left:568px">CATEGORY</a>
    <a href="#" style="left:654px">PROFILE</a>
    <a href="#" style="left:727px">APPLY FOR JOB</a>
    <a href="#" style="left:843px">SEARCH</a>
    <a href="#" style="left:914px">CONTACTS</a>
    <a class="sign-in" href="#" style="left:1001px">SIGN IN</a>
  </nav>
</header>

<section class="hero">
  <div class="hero-photo" role="img" aria-label="Photo of a tradeswoman in a yellow hard hat wearing a tool belt"></div>
  <h1 class="hero-title"><strong>Easy To Find</strong> Reliable Business Man<br>Handyman&nbsp; or <strong>Builder</strong>.</h1>
  <p class="hero-copy">Lorem ipsum dolor sit amet, consectetur adipisicing elit, sed do eiusmod tempor incididunt ut labore et dolore magna aliqua. Lorem incididunt ut labore et dolore magna aliqua. Lorem ipsum dolor sit amet, consectetur adipisicing elit.</p>
  <a class="hero-button" href="#"><span>View all info</span></a>
  <div class="slider-dots"><i></i><i></i><i></i></div>
</section>

<div class="shade-line"></div>

<section class="about">
  <h2>About us</h2>
  <p>Lorem ipsum dolor sit amet, consectetur adipiscing elit. Integer dictum, neque ut imperdiet pellentesque, nulla tellus tempus. Lorem ipsum dolor sit amet, consectetur adipiscing elit. Integer dictum, neque ut imperdiet pellentesque, ut imperdiet pellentesque, nulla tellus tempus. Lorem ipsum dolor sit amet, nulla tellus tempus. Pellentesque diam sagittis ullamcorper.</p>
</section>

<form class="finder">
  <p class="finder-title">Ready to find a tradesman? <strong>Start Here!</strong></p>
  <label style="left:25px;top:56px">Description</label>
  <div class="field" style="left:110px;top:55px;width:92px"></div>
  <label style="left:218px;top:56px">Max price</label>
  <div class="field select" style="left:291px;top:56px;width:92px">Select</div>
  <label style="left:25px;top:92px">Date</label>
  <div class="field select" style="left:111px;top:86px;width:92px">Select</div>
  <label style="left:217px;top:92px">Duration</label>
  <div class="field select" style="left:291px;top:95px;width:92px">Select</div>
  <label style="left:25px;top:128px">Location</label>
  <div class="field" style="left:93px;top:120px;width:112px"></div>
  <a class="finder-submit" href="#">find a tradesman <strong>NOW!</strong></a>
</form>

<div class="divider"></div>

<article class="feature" style="left:151px">
  <div class="feature-icon" role="img" aria-label="Small worker figure icon"></div>
  <h3>Tradesmen Ratings</h3>
  <p>consectetur adipiscing elit. Integer dictum, neque ut imperdiet pellentesque, nulla tellus tempus. Pellentesque diam sagittis ullamcorper.</p>
</article>
<article class="feature" style="left:469px;width:245px">
  <div class="feature-icon" role="img" aria-label="Small builder figure icon"></div>
  <h3 style="margin-left:30px;margin-top:1px">Builder Service</h3>
  <p style="margin-top:23px">Tonsectetur adipiscing elit. Integer dictum, neque ut imperdiet pellentesque, nulla tellus tempus. Pellentesque diam sagittis.</p>
</article>
<article class="feature" style="left:799px">
  <div class="feature-icon" role="img" aria-label="Small local tradesman figure icon"></div>
  <h3 style="margin-left:25px;margin-top:-1px">Local Tradesman</h3>
  <p class="callout" style="margin-top:24px">Interested tradesman will contacts you Shortly.</p>
</article>

<footer class="site-footer">
  <div class="contacts">
    <h4>CONTACTS INFO</h4>
    <p>48 Marlow Street Brookvale, Sydney<br>NSW Australia - 20145.<br><b>Phone----</b> 95550142<br><b>Fax--------</b> 0400 555 218 36</p>
  </div>
  <div class="message">
    <h4>SEND US A MESSAGE</h4>
    <div class="input" style="left:2px;top:37px;width:237px;height:26px">Your Name</div>
    <div class="input" style="left:2px;top:73px;width:237px;height:26px">Your Email</div>
    <div class="input" style="left:2px;top:109px;width:357px;height:79px">Your message goes here</div>
    <a class="submit-btn" href="#">SUBMIT</a>
  </div>
  <div class="follow">
    <h4>FOLLOW ME</h4>
    <ul>
      <li><i></i>Follow Us on Chirper</li>
      <li><i></i>Follow Us on Friendbook</li>
    </ul>
  </div>
  <div class="legal">
    <p class="copy">Copyright 2011 fixwell-trades.com</p>
    <nav>HOME<span>/</span>TERMS OF USE<span>/</span>PRIVACY<span>/</span>HELP<span>/</span>CONTACTS</nav>
  </div>
</footer>

</div>
</body>
</html>
```